Wealth management Facebook Advertisement

Hello, we are trying to capture more leads to our online booking link through Facebook advertisement. We want an attractive modern design to get more clients and catch the attention of high net-worth clients. We deal with high-net-worth retirees, business owners, farmers, and wealth transfer. We offer high-net-worth client solutions that cover Financial Planning, Retirement and Estate Planning, Investment Planning, Tax Planning, and Insurance Planning. The final design that we would be looking for is modern and eye-catching and makes the prospective clients want to click our meeting link to schedule an introductory consultation.

We are in the Wealth Management / Financial Planning industry

Our online booking link Is the following :

https://bookings.qvnfinancial-demo.net/calendar/OliverBrandtAssociatesQLPrivateWealth@qvnfinancial-demo.net/bookings/

Our current Facebook page is the following:

https://www.sociopage-demo.net/BrandtPrivateWealth

Please ask any further questions for needed information for creating design

```html
<!DOCTYPE html>
<html lang="en">
<head>
<meta charset="utf-8">
<title>Unlock Your Financial Potential – Oliver Brandt &amp; Associates</title>
<link rel="stylesheet" href="https://fonts.googleapis.com/css2?family=Oswald:wght@500;600;700&family=Roboto:wght@500&display=swap">
<style>
  :root{
    --bg:#f3f4f6;
    --stripe:#fafbfc;
    --navy:#0d2566;
    --ink:#0f2b6e;
    --blue:#1a6fd6;
    --white:#ffffff;
    --sky-top:#eaf3fb;
    --sky-mid:#b9d2ea;
    --sky-low:#4f7fae;
  }
  html,body{margin:0;padding:0;overflow:hidden;}
  .ad{
    position:relative;width:1200px;height:1200px;overflow:hidden;
    background:
      repeating-linear-gradient(-45deg, transparent 0 110px, var(--stripe) 110px 160px, transparent 160px 260px),
      var(--bg);
    font-family:'Oswald',sans-serif;
  }
  .art{position:absolute;inset:0;}
  .brand{
    position:absolute;left:42px;top:44px;display:flex;gap:12px;align-items:flex-start;
  }
  .brand-square{width:40px;height:40px;background:var(--ink);margin-top:2px;}
  .brand-name{
    font-family:'Roboto',sans-serif;font-weight:500;color:var(--ink);
    font-size:18px;line-height:19px;text-transform:uppercase;
  }
  .headline{
    position:absolute;left:322px;top:98px;width:561px;text-align:center;color:var(--ink);
  }
  .headline .lead{font-size:62px;font-weight:600;line-height:66px;margin:0;}
  .headline .main{font-size:69px;font-weight:700;line-height:72px;margin:0;}
  .headline .sub{font-size:33px;font-weight:500;line-height:40px;margin:4px 0 0;}
  .cta-text{
    position:absolute;left:52px;top:1038px;color:var(--white);
    font-size:32px;font-weight:700;line-height:34px;text-transform:uppercase;
  }
  .cta-rule{position:absolute;left:55px;top:1154px;width:188px;height:5px;background:var(--blue);}
  .book-btn{
    position:absolute;left:917px;top:1030px;width:228px;height:74px;box-sizing:border-box;
    border:2px solid var(--white);border-radius:14px;background:var(--blue);
    color:var(--white);font-size:40px;font-weight:600;display:flex;align-items:center;justify-content:center;
    text-decoration:none;
  }
  .book-note{
    position:absolute;left:907px;top:1110px;width:248px;text-align:center;color:var(--white);
    font-size:24px;font-weight:600;white-space:nowrap;
  }
</style>
</head>
<body>
<div class="ad">
  <svg class="art" width="1200" height="1200" viewBox="0 0 1200 1200">
    <defs>
      <linearGradient id="sky" x1="0" y1="0" x2="0" y2="1">
        <stop offset="0" stop-color="var(--sky-top)"/>
        <stop offset="0.45" stop-color="var(--sky-mid)"/>
        <stop offset="1" stop-color="var(--sky-low)"/>
      </linearGradient>
      <path id="service-arc" d="M229,752 A372,372 0 1,1 971,752"/>
    </defs>

    <g class="headline-frame" fill="none" stroke="var(--ink)" stroke-width="2">
      <polyline points="445,126 322,126 322,262 352,262"/>
      <polyline points="760,126 883,126 883,262 856,262"/>
    </g>

    <g class="base" fill="var(--navy)">
      <circle cx="600" cy="720" r="335"/>
      <path d="M0,985 C150,985 250,930 285,835 L915,835 C950,930 1050,975 1200,975 L1200,1200 L0,1200 Z"/>
    </g>
    <circle class="ring" cx="600" cy="720" r="323" fill="var(--blue)"/>
    <circle class="photo" cx="600" cy="720" r="303" fill="url(#sky)" role="img"
      aria-label="Photo of a businessman in a suit seen from behind, looking up at glass skyscrapers"/>

    <text font-family="Oswald, sans-serif" font-weight="700" font-size="22" fill="var(--ink)" letter-spacing="1">
      <textPath href="#service-arc" startOffset="50%" text-anchor="middle" textLength="1215" lengthAdjust="spacing">FINANCIAL PLANNING | RETIREMENT AND ESTATE PLANNING | INVESTMENT PLANNING / TAX PLANNING / INSURANCE PLANNING</textPath>
    </text>

    <g class="icons" fill="none" stroke="var(--ink)" stroke-width="2" stroke-linecap="round" stroke-linejoin="round">
      <g>
        <line x1="1048" y1="262" x2="1118" y2="262"/>
        <rect x="1055" y="225" width="12" height="37"/>
        <rect x="1069" y="212" width="30" height="50"/>
        <rect x="1101" y="202" width="12" height="60"/>
        <line x1="1090" y1="228" x2="1078" y2="250"/>
        <circle cx="1079" cy="230" r="3"/>
        <circle cx="1089" cy="248" r="3"/>
      </g>
      <g>
        <circle cx="173" cy="416" r="13"/>
        <circle cx="194" cy="432" r="13"/>
        <path d="M158,448 L220,428 L190,476 L180,458 Z M180,458 L220,428"/>
        <text x="173" y="422" font-size="16" fill="var(--ink)" stroke="none" text-anchor="middle" font-family="Oswald, sans-serif">$</text>
        <text x="194" y="438" font-size="16" fill="var(--ink)" stroke="none" text-anchor="middle" font-family="Oswald, sans-serif">$</text>
      </g>
      <g>
        <path d="M70,822 L120,822 L120,866 Q120,876 110,876 L62,876 Q56,876 56,868 L70,868 L70,822 Z"/>
        <path d="M120,822 Q126,822 126,830 L120,830"/>
        <line x1="88" y1="836" x2="112" y2="836"/>
        <line x1="88" y1="848" x2="112" y2="848"/>
        <line x1="88" y1="860" x2="112" y2="860"/>
        <line x1="66" y1="850" x2="80" y2="836"/>
        <circle cx="67" cy="838" r="2.5"/>
        <circle cx="79" cy="849" r="2.5"/>
      </g>
      <g>
        <path d="M1072,800 L1090,784 L1108,800 M1076,797 L1076,816 L1104,816 L1104,797"/>
        <rect x="1085" y="803" width="10" height="13"/>
        <path d="M1052,828 L1066,822 Q1074,820 1082,826 L1096,826 Q1102,828 1096,834 L1082,834 M1096,830 L1110,820 Q1118,816 1116,826 L1098,846 L1066,846 L1058,850"/>
      </g>
    </g>
  </svg>

  <div class="brand">
    <div class="brand-square"></div>
    <div class="brand-name">Northvale<br>Wealth Partners<br>Oliver Brandt<br>&amp; Associates</div>
  </div>

  <div class="headline">
    <p class="lead">Unlock Your</p>
    <p class="main">Financial Potential</p>
    <p class="sub">Your Path to Prosperity Begins Here!</p>
  </div>

  <div class="cta-text">Schedule a<br>Consultation<br>Today!</div>
  <div class="cta-rule"></div>

  <a class="book-btn" href="https://bookings.qvnfinancial-demo.net/calendar/OliverBrandtAssociatesQLPrivateWealth@qvnfinancial-demo.net/bookings/">BOOK NOW</a>
  <div class="book-note">LINK IN DESCRIPTION</div>
</div>
</body>
</html>
```